Four in One (Flexible infographic for Content Management Industry)

See attachment.
A graphic depicting 4 products, where each can stand on its own and each can be combined with others, but where, if all are taken together, the best result is achieved (the "super product").
Intended use is web. See attached file as an example.
The most basic idea is as the attached diagram shows, where 4 rectangles are arranged in a quadrangle, with a middle rectangle in the center representing the combined 4 products. This concept is fine except it is a bit too obvious as it stands. We are looking for either a variation of this or another concept.
The audience is technical + professional + enterprise - NOT consumers. Hence the design should be conservative in nature.
We are aware of tools like as Canva or Pictogram where such graphics are available, but we are looking for something with a bit more imagination and flexibility.
This graphic should be targeted to web sites and be delivered with vector-based (SVG) graphics.

```html
<!DOCTYPE html>
<html lang="en">
<head>
<meta charset="utf-8">
<title>Super Product – Four in One</title>
<link rel="stylesheet" href="https://fonts.googleapis.com/css2?family=Fira+Sans+Condensed:ital,wght@0,300;0,400;0,500;0,600;1,400&family=Fira+Sans+Extra+Condensed:wght@800&display=swap">
<style>
  :root {
    --purple: #6c4fbd;
    --red: #ff4320;
    --blue: #4a5ff8;
    --orange: #ffa106;
    --card: #e9f4fb;
    --hub: #f1f1f1;
    --ink: #2b2b2b;
    --rule: #9c9c9c;
    --button: #a68bc0;
  }
  * { box-sizing: border-box; margin: 0; padding: 0; }
  html, body { width: 1200px; height: 768px; overflow: hidden; background: #fff; }
  body { position: relative; font-family: "Fira Sans Condensed", sans-serif; color: var(--ink); }
  .shapes { position: absolute; inset: 0; }
  .card-shape { fill: var(--card); filter: drop-shadow(3px 5px 6px rgba(0,0,0,.35)); }
  .hub { fill: var(--hub); stroke: #fff; stroke-width: 9; filter: drop-shadow(0 3px 8px rgba(0,0,0,.25)); }

  .module { position: absolute; width: 320px; }
  .module--left { left: 154px; }
  .module--right { left: 734px; width: 312px; text-align: right; }
  .module--top { top: 124px; }
  .module--bottom { top: 451px; }

  .module__title { font-size: 23px; font-weight: 500; line-height: 26px; letter-spacing: -.2px; white-space: nowrap; }
  .module__text { font-size: 12.2px; font-weight: 300; line-height: 16.5px; margin-top: 2px; text-align: left; }
  .module__rule { height: 2px; background: linear-green; margin: 10px 0 10px; background: linear-gradient(90deg, var(--rule), rgba(156,156,156,0)); width: 300px; }
  .module--right .module__rule { background: linear-gradient(270deg, var(--rule), rgba(156,156,156,0)); margin-left: auto; }
  .module__list { list-style: none; font-size: 11.8px; font-style: italic; line-height: 16.7px; }
  .module__list li::before { content: "✓ "; font-style: normal; }
  .module--right .module__list li::before { content: none; }
  .module--right .module__list li::after { content: " ✓"; font-style: normal; }
  .module__button { display: inline-flex; align-items: center; gap: 3px; margin-top: 8px; height: 19px; padding: 0 6px 0 8px; border-radius: 3px; background: var(--button); box-shadow: 0 2px 0 #7b6690; color: #fff; font-size: 8.5px; font-weight: 600; letter-spacing: .3px; }
  .module__button svg { width: 9px; height: 9px; }

  .module--purple .module__title { color: var(--purple); }
  .module--red .module__title { color: var(--red); }
  .module--blue .module__title { color: var(--blue); }
  .module--orange .module__title { color: var(--orange); }
  .module--orange .module__title { color: var(--red); }

  .hub-label { position: absolute; left: 450px; top: 334px; width: 300px; text-align: center; font-family: "Fira Sans Extra Condensed", sans-serif; font-weight: 800; font-size: 46px; line-height: 39px; color: #222; letter-spacing: -.5px; }
</style>
</head>
<body>
<svg class="shapes" width="1200" height="768" viewBox="0 0 1200 768" aria-hidden="true">
  <defs>
    <path id="block" d="M87,85 H532 Q587,85 587,140 V360 H147 Q87,360 87,300 Z"/>
    <path id="card" d="M142,100 H467 Q497,100 497,130 V218 Q497,240 480,252 Q450,272 435,310 Q428,328 405,328 H142 Q112,328 112,298 V130 Q112,100 142,100 Z"/>
  </defs>
  <use href="#block" fill="var(--purple)"/>
  <use href="#block" fill="var(--red)" transform="translate(1205,0) scale(-1,1)"/>
  <use href="#block" fill="var(--blue)" transform="translate(0,755) scale(1,-1)"/>
  <use href="#block" fill="var(--orange)" transform="translate(1205,755) scale(-1,-1)"/>

  <use href="#card" class="card-shape"/>
  <use href="#card" class="card-shape" transform="translate(1199,0) scale(-1,1)"/>
  <use href="#card" class="card-shape" transform="translate(0,756) scale(1,-1)"/>
  <use href="#card" class="card-shape" transform="translate(1199,756) scale(-1,-1)"/>

  <!-- icon tabs -->
  <g>
    <path d="M112,129 H135 Q145,129 145,139.5 Q145,150 135,150 H112 Z" fill="var(--purple)"/>
    <rect x="124" y="134" width="9" height="11" rx="1" fill="none" stroke="#fff" stroke-width="1.2"/>
    <path d="M126,138 h5 M126,140.5 h5 M126,143 h3" stroke="#fff" stroke-width="1"/>
  </g>
  <g>
    <path d="M1087,129 H1064 Q1054,129 1054,139.5 Q1054,150 1064,150 H1087 Z" fill="var(--red)"/>
    <path d="M1064,144 h15 a4,4 0 0 0 0-8 a5.5,5.5 0 0 0-10.5-1 a3.8,3.8 0 0 0-4.5,9 Z" fill="none" stroke="#fff" stroke-width="1.3"/>
    <path d="M1071,146 v-7 M1068.5,141.5 l2.5-2.5 l2.5,2.5" fill="none" stroke="#fff" stroke-width="1.3"/>
  </g>
  <g>
    <path d="M112,454 H135 Q145,454 145,464.5 Q145,475 135,475 H112 Z" fill="var(--blue)"/>
    <rect x="123" y="458" width="12" height="12" rx="1" fill="none" stroke="#fff" stroke-width="1.2"/>
    <path d="M126,467 v-3 M129,467 v-5 M132,467 v-2" stroke="#fff" stroke-width="1.3"/>
  </g>
  <g>
    <path d="M1087,454 H1064 Q1054,454 1054,464.5 Q1054,475 1064,475 H1087 Z" fill="var(--orange)"/>
    <circle cx="1071" cy="464.5" r="3" fill="none" stroke="#fff" stroke-width="1.3"/>
    <path d="M1071,457 v3 M1071,469 v3 M1063.5,464.5 h3 M1075.5,464.5 h3 M1066,459.5 l2,2 M1074,467.5 l2,2 M1076,459.5 l-2,2 M1068,467.5 l-2,2" stroke="#fff" stroke-width="1.3"/>
  </g>

  <circle class="hub" cx="600" cy="377" r="145"/>
</svg>

<section class="module module--left module--top module--purple">
  <h2 class="module__title">Document Management</h2>
  <p class="module__text">Streamline document organization, access, and collaboration with easier file storage and sharing, leading to more efficient workflows.</p>
  <div class="module__rule"></div>
  <ul class="module__list">
    <li>Centralized Document Control</li>
    <li>Collaborative Workspace Integration</li>
    <li>Automated Compliance Tracking</li>
    <li>Check 4</li>
  </ul>
  <span class="module__button">LEARN MORE <svg viewBox="0 0 10 10"><circle cx="5" cy="5" r="4.2" fill="none" stroke="#fff"/><path d="M4,3 L6,5 L4,7" fill="none" stroke="#fff"/></svg></span>
</section>

<section class="module module--right module--top module--red">
  <h2 class="module__title">Security and Compliance</h2>
  <p class="module__text">Benefit from tailored cloud solutions, secure data storage, and expert disaster recovery planning for reliable and scalable IT operations.</p>
  <div class="module__rule"></div>
  <ul class="module__list">
    <li>Custom Cloud Solutions</li>
    <li>Secure Data Storage</li>
    <li>Expert Disaster Recovery</li>
    <li>Check 4</li>
  </ul>
  <span class="module__button">LEARN MORE <svg viewBox="0 0 10 10"><circle cx="5" cy="5" r="4.2" fill="none" stroke="#fff"/><path d="M4,3 L6,5 L4,7" fill="none" stroke="#fff"/></svg></span>
</section>

<section class="module module--left module--bottom module--blue">
  <h2 class="module__title">Enterprise Resource Planning</h2>
  <p class="module__text" style="width:260px">Simplify management across finance, sales, and operations, enabling better decision-making and improved productivity.</p>
  <div class="module__rule"></div>
  <ul class="module__list">
    <li>Integrated Business Processes</li>
    <li>Enhanced Decision-Making</li>
    <li>Productivity Improvement</li>
    <li>Check 4</li>
  </ul>
  <span class="module__button">LEARN MORE <svg viewBox="0 0 10 10"><circle cx="5" cy="5" r="4.2" fill="none" stroke="#fff"/><path d="M4,3 L6,5 L4,7" fill="none" stroke="#fff"/></svg></span>
</section>

<section class="module module--right module--bottom module--orange">
  <h2 class="module__title">Security and Compliance</h2>
  <p class="module__text" style="margin-left:38px">Turn scanned documents into easily searchable digital archives, boosting efficiency and accessibility.</p>
  <div class="module__rule" style="margin-top:28px"></div>
  <ul class="module__list">
    <li>Instant searchable Archives with OCR</li>
    <li>Automated Document Classification</li>
    <li>DocuHub and Cloud Blob Ready</li>
    <li>Check 4</li>
  </ul>
  <span class="module__button">LEARN MORE <svg viewBox="0 0 10 10"><circle cx="5" cy="5" r="4.2" fill="none" stroke="#fff"/><path d="M4,3 L6,5 L4,7" fill="none" stroke="#fff"/></svg></span>
</section>

<h1 class="hub-label">SUPER<br>PRODUCT</h1>
</body>
</html>
```